Hensby Estates Website and Logo Design

We need a new logo and website designed for 'Hensby Estates Ltd', which is a well established Guernsey property holding company founded in 1934.

The company does not currently have a website. The new website should be similar in style and layout to https://www.corvanhale.org/.

Target Market(s)

Industry, Media, Tenants

Industry/Entity Type

Property Management

Logo Text

HEL OR Hensby Estates Ltd OR HE

Coding

Coded - Design and coding required

Number of Pages Required

4 page

Font styles to use
Other font styles liked:
• Helvetica

Requirements
Must have
• The logo laying over the picture (like https://www.corvanhale.org/).
• Big pictures on homepage (like https://www.corvanhale.org/)

```html
<!DOCTYPE html>
<html lang="en">
<head>
<meta charset="utf-8">
<title>Hensby Estates Limited</title>
<link rel="stylesheet" href="https://fonts.googleapis.com/css2?family=Oswald:wght@400;500&family=Open+Sans:wght@400;600;700&family=Roboto:wght@400;500&display=swap">
<style>
:root{
  --blue:#2f5aa8;
  --ink:#333;
  --muted:#555;
  --light:#f0f0f0;
  --white:#fff;
  --footer-bar:#2f5fb3;
}
*{box-sizing:border-box;margin:0;padding:0}
html,body{width:1200px;height:2635px;overflow:hidden}
body{position:relative;background:var(--white);font-family:"Open Sans",Arial,sans-serif;color:var(--ink)}
.abs{position:absolute}
.center{left:0;width:1200px;text-align:center}
.heading{font-family:"Oswald",Arial,sans-serif;font-weight:400;color:var(--blue)}

/* hero */
.hero{left:0;top:0;width:1200px;height:605px;background:linear-gradient(180deg,#6d8fbf 0%,#5a80b6 30%,#33558a 52%,#2f4f80 75%,#3c5c8a 100%)}
.hero-cut{left:0;top:520px}
.brand{left:100px;top:38px;display:flex;align-items:center;gap:12px;font-family:"Oswald",Arial,sans-serif;font-size:26px;color:var(--white)}
.brand-square{width:40px;height:40px;border:3px solid var(--white)}
.topline{right:97px;top:21px;display:flex;align-items:center;gap:8px;color:var(--white);font-size:17px;font-weight:600}
.ring{width:32px;height:32px;border:2px solid var(--white);border-radius:50%;display:inline-block}
.topline .call{margin-right:24px;display:flex;align-items:center;gap:10px}
.nav{right:98px;top:80px;display:flex;gap:35px;color:var(--white);font-size:15px;font-weight:600}
.nav .last{margin-left:18px}
.hero-title{top:180px;font-family:"Oswald",Arial,sans-serif;font-weight:400;font-size:48px;color:var(--white)}
.hero-sub{top:270px;left:220px;width:760px;text-align:center;color:var(--white);font-size:16px;font-weight:600;line-height:28px}
.hero-btn{left:538px;top:362px;width:124px;height:44px;background:var(--white);color:var(--blue);font-size:15px;font-weight:600;display:flex;align-items:center;justify-content:center}
.dots{left:554px;top:537px;display:flex;gap:4px}
.dots span{width:16px;height:16px;border:2px solid var(--white);border-radius:50%}

/* shared */
.section-title{font-size:30px}
.rule{height:2px;width:140px;background:var(--blue);left:530px}
.body-text{font-size:12.5px;line-height:23px;color:var(--muted)}
.btn{height:44px;display:flex;align-items:center;justify-content:center;font-family:"Roboto",Arial,sans-serif;font-size:15px;border-radius:2px}
.btn-solid{background:var(--blue);color:var(--white)}
.btn-line{border:1.5px solid #555;color:var(--ink);background:var(--white)}

/* properties */
.properties{left:0;top:937px;width:1200px;height:593px;background:var(--light)}
.card{top:1096px;width:313px;height:394px;background:var(--white);box-shadow:0 3px 6px rgba(0,0,0,.25);border-bottom:3px solid #444}
.card.active{border-bottom-color:var(--blue)}
.card-photo{width:313px;height:195px}
.card h3{margin-top:20px;text-align:center;font-size:20px;font-weight:600;color:var(--blue)}
.card p{margin:10px 16px 0;text-align:center;font-size:12.5px;line-height:23px;color:var(--muted)}
.card .btn{position:absolute;left:96px;top:332px;width:121px;height:37px;font-size:14px}

/* about */
.about{left:0;top:1530px;width:1200px;height:390px;background:linear-gradient(180deg,#2f59a5,#2a509a)}
.about-title{left:98px;top:1568px;font-family:"Oswald",Arial,sans-serif;font-weight:400;font-size:29px;color:var(--white)}
.about-text{left:98px;top:1626px;width:510px;color:var(--white);font-size:12.5px;line-height:25px}
.checks{color:var(--white);font-size:17px;display:flex;align-items:center;gap:14px}
.video{left:697px;top:1578px;width:401px;height:267px;border:4px solid #e8eef8;box-shadow:0 6px 14px rgba(0,0,0,.35);background:linear-gradient(180deg,#4f7dc2 0%,#7fa3d6 40%,#3a6aa0 55%,#1f4a7c 100%)}
.play{left:180px;top:110px}
.video-bar{left:0;bottom:0;width:393px;height:26px;background:rgba(20,30,50,.75)}
.video-bar i{position:absolute;left:20px;top:11px;width:110px;height:4px;background:#3fa0e0}

/* testimonials */
.avatar{width:120px;height:120px;border-radius:50%;border:3px solid var(--blue);background:radial-gradient(circle at 50% 45%,#e8d6c8,#b89a86 70%,#8d7a70)}
.t-title{font-family:"Roboto",Arial,sans-serif;font-size:22px;color:#222}
.t-sub{font-family:"Roboto",Arial,sans-serif;font-size:15px;color:#666}
.stars{font-size:17px;color:var(--blue);letter-spacing:2px}
.t-text{font-size:12.5px;line-height:23px;color:var(--muted);width:490px}

/* footer */
.footer{left:0;top:2275px;width:1200px;height:307px;border-top:3px solid var(--blue);background:linear-gradient(135deg,#f1f2ef,#e7e9e4 50%,#eef0ec)}
.f-brand{left:98px;top:2372px;width:226px;text-align:center;font-family:"Oswald",Arial,sans-serif;font-size:25px;color:var(--blue)}
.f-square{width:54px;height:54px;border:4px solid var(--blue);margin:0 auto 24px}
.f-head{font-family:"Open Sans",Arial,sans-serif;font-weight:700;font-size:20px;color:#222;letter-spacing:.5px}
.f-list{list-style:none;font-size:14px;color:#333}
.f-list li{height:27.5px;display:flex;align-items:center;gap:12px}
.f-list .chev{width:10px;font-size:15px}
.f-social li{height:36px}
.f-circle{width:26px;height:26px;border:1.5px solid #333;border-radius:50%;display:inline-block}
.contact-row{display:flex;gap:16px}
.contact-icon{width:38px;height:38px;border:1.5px solid #333;border-radius:50%;display:flex;align-items:center;justify-content:center;flex:none}
.contact-row b{display:block;font-size:15px;font-weight:700;color:#222}
.contact-row span{font-size:13px;color:#444;line-height:22px}
.footer-bar{left:0;top:2582px;width:1200px;height:53px;background:var(--footer-bar);color:var(--white);font-size:14px;font-weight:600;display:flex;align-items:center;justify-content:center}
</style>
</head>
<body>

<div class="abs hero" role="img" aria-label="Harbour photograph with moored boats and rocky islets under a blue sky"></div>
<svg class="abs hero-cut" width="1200" height="90" viewBox="0 0 1200 90">
  <polygon points="0,7 600,81 1200,7 1200,90 0,90" fill="#fff"/>
  <polyline points="0,7 600,81 1200,7" fill="none" stroke="#2f5aa8" stroke-width="3"/>
</svg>

<div class="abs brand"><span class="brand-square"></span>Hensby Estates Limited</div>
<div class="abs topline">
  <span class="call">
    <span class="ring" style="display:flex;align-items:center;justify-content:center">
      <svg width="16" height="16" viewBox="0 0 24 24"><path d="M6.6 10.8a15 15 0 0 0 6.6 6.6l2.2-2.2a1 1 0 0 1 1-.25 11 11 0 0 0 3.6.6 1 1 0 0 1 1 1V20a1 1 0 0 1-1 1A17 17 0 0 1 3 4a1 1 0 0 1 1-1h3.5a1 1 0 0 1 1 1 11 11 0 0 0 .6 3.6 1 1 0 0 1-.25 1z" fill="#fff"/></svg>
    </span>
    CALL US AT: 180 047 9312
  </span>
  <span class="ring"></span><span class="ring"></span><span class="ring"></span><span class="ring"></span><span class="ring"></span>
</div>
<nav class="abs nav"><span>Home</span><span>About</span><span>Why Choose Us</span><span>Videos</span><span>Events</span><span class="last">Contact Us</span></nav>

<h1 class="abs center hero-title">HENSBY ESTATES LIMITED</h1>
<p class="abs hero-sub">Nemo enim ipsam voluptatem quia voluptas sit aspernatur aut odit aut fugit, sed quia consequuntur magni dolores eos qui ratione voluptatem</p>
<div class="abs hero-btn">READ MORE</div>
<div class="abs dots"><span></span><span></span><span></span><span></span><span></span></div>

<h2 class="abs center heading section-title" style="top:645px">Welcome To Hensby Estates Limited</h2>
<div class="abs rule" style="top:700px"></div>
<p class="abs body-text" style="left:160px;width:880px;top:727px;text-align:center">Nemo enim ipsam voluptatem quia voluptas sit aspernatur aut odit aut fugit, sed quia consequuntur magni dolores eos qui ratione voluptatem sequi nesciunt. Neque porro quisquam est, qui dolorem ipsum quia dolor sit amet, consectetur, adipisci velit, sed quia non numquam eius modi tempora incidunt ut labore et dolore magnam aliquam quaerat voluptatem. Ut enim ad minima veniam, quis nostrum exercitationem ullam corporis suscipit laboriosam, nisi ut aliquid ex ea commodi consequatur.</p>
<div class="abs btn btn-solid" style="left:457px;top:850px;width:133px">Read More</div>
<div class="abs btn btn-line" style="left:610px;top:850px;width:135px">Contact Us</div>

<div class="abs properties"></div>
<h2 class="abs center heading section-title" style="top:966px">Our Properties</h2>
<p class="abs body-text" style="left:160px;width:880px;top:1019px;text-align:center">Nemo enim ipsam voluptatem quia voluptas sit aspernatur aut odit aut fugit, sed quia consequuntur magni dolores eos qui ratione voluptatem sequi nesciunt. Neque porro quisquam est, qui dolorem ipsum quia dolor sit amet.</p>

<article class="abs card active" style="left:98px">
  <div class="card-photo" role="img" aria-label="Harbour with a pier, moored boats and a distant island" style="background:linear-gradient(180deg,#9fb6cf 0%,#7d98b5 35%,#3f7f86 55%,#2f6e78 100%)"></div>
  <h3>Voluptatem Accusantium</h3>
  <p>Donec sodales sagittis magna. Sed consequat, leo eget bibendum sodales, augue velit and setld tasm cursus nunc.</p>
  <div class="btn btn-solid">View Details</div>
</article>
<article class="abs card" style="left:443px">
  <div class="card-photo" role="img" aria-label="Marina full of boats below a hillside town" style="background:linear-gradient(180deg,#7f9fcc 0%,#a7b6c8 35%,#8b8f92 60%,#3f5d77 100%)"></div>
  <h3>Nostrum Exercitationem</h3>
  <p>Donec sodales sagittis magna. Sed consequat, leo eget bibendum sodales, augue velit and setld tasm cursus nunc.</p>
  <div class="btn btn-line">View Details</div>
</article>
<article class="abs card" style="left:789px">
  <div class="card-photo" role="img" aria-label="Seaside village with white houses around a harbour" style="background:linear-gradient(180deg,#4e84cc 0%,#8fb0da 30%,#c9cbc4 48%,#2f7f8c 62%,#1f5f78 100%)"></div>
  <h3>Neque Porro Quisquam</h3>
  <p>Donec sodales sagittis magna. Sed consequat, leo eget bibendum sodales, augue velit and setld tasm cursus nunc.</p>
  <div class="btn btn-line">View Details</div>
</article>

<section class="abs about"></section>
<h2 class="abs about-title">About Hensby Estates Limited</h2>
<p class="abs about-text">Neque porro quisquam est, qui dolorem ipsum quia dolor sit amet, consectetur, adipisci velit, sed quia non numquam eius modi tempora incidunt ut labore et dolore magnam aliquam quaerat voluptatem. Ut enim ad minima veniam, quis nostrum exercitationem</p>

<svg width="0" height="0" style="position:absolute"><symbol id="tick" viewBox="0 0 28 28"><rect x="2" y="5" width="20" height="20" rx="3" fill="none" stroke="#fff" stroke-width="2.5"/><path d="M7 14l5 5L26 3" fill="none" stroke="#fff" stroke-width="3.5" stroke-linecap="round"/></symbol></svg>
<div class="abs checks" style="left:100px;top:1757px"><svg width="28" height="28"><use href="#tick"/></svg>Maintenance</div>
<div class="abs checks" style="left:100px;top:1799px"><svg width="28" height="28"><use href="#tick"/></svg>Collecting rent</div>
<div class="abs checks" style="left:100px;top:1841px"><svg width="28" height="28"><use href="#tick"/></svg>Managing Properties</div>
<div class="abs checks" style="left:339px;top:1757px"><svg width="28" height="28"><use href="#tick"/></svg>Income</div>
<div class="abs checks" style="left:339px;top:1799px"><svg width="28" height="28"><use href="#tick"/></svg>Property Preservation</div>
<div class="abs checks" style="left:339px;top:1841px"><svg width="28" height="28"><use href="#tick"/></svg>Administration</div>

<div class="abs video" role="img" aria-label="Video still of a bay with small boats and rocky islands">
  <svg class="abs play" width="48" height="48" viewBox="0 0 48 48"><circle cx="24" cy="24" r="22" fill="rgba(0,0,0,.35)" stroke="#fff" stroke-width="3"/><polygon points="19,14 35,24 19,34" fill="#fff"/></svg>
  <div class="abs video-bar"><i></i></div>
</div>

<h2 class="abs center heading section-title" style="top:1952px">Client Testimonials</h2>
<div class="abs rule" style="left:552px;width:96px;top:2008px"></div>

<div class="abs avatar" style="left:98px;top:2052px" role="img" aria-label="Client portrait"></div>
<svg class="abs" style="left:238px;top:2062px" width="28" height="24" viewBox="0 0 28 24"><rect x="0" y="0" width="11" height="13" fill="#2f5aa8"/><path d="M0 13 L11 13 L4 24 Z" fill="#2f5aa8"/><rect x="15" y="0" width="11" height="13" fill="#2f5aa8"/><path d="M15 13 L26 13 L19 24 Z" fill="#2f5aa8"/></svg>
<div class="abs t-title" style="left:283px;top:2061px">Good Property Preservation</div>
<div class="abs t-sub" style="left:283px;top:2097px">Hensby Estates</div>
<div class="abs stars" style="left:282px;top:2130px">★★★★☆</div>
<p class="abs t-text" style="left:98px;top:2188px">Neque porro quisquam est, qui dolorem ipsum quia dolor sit amet, consecte tur, adipisci velit, sed quia non numquam eius modi tempora.</p>

<div class="abs avatar" style="left:627px;top:2052px" role="img" aria-label="Client portrait"></div>
<svg class="abs" style="left:766px;top:2062px" width="28" height="24" viewBox="0 0 28 24"><rect x="0" y="0" width="11" height="13" fill="#2f5aa8"/><path d="M0 13 L11 13 L4 24 Z" fill="#2f5aa8"/><rect x="15" y="0" width="11" height="13" fill="#2f5aa8"/><path d="M15 13 L26 13 L19 24 Z" fill="#2f5aa8"/></svg>
<div class="abs t-title" style="left:811px;top:2061px">Good Property Preservation</div>
<div class="abs t-sub" style="left:811px;top:2097px">Hensby Estates</div>
<div class="abs stars" style="left:810px;top:2130px">★★★★☆</div>
<p class="abs t-text" style="left:627px;top:2188px">Neque porro quisquam est, qui dolorem ipsum quia dolor sit amet, consecte tur, adipisci velit, sed quia non numquam eius modi tempora.</p>

<footer class="abs footer" role="img" aria-label="Faint regional map in the background"></footer>
<div class="abs f-brand"><div class="f-square"></div>Hensby Estates Limited</div>

<div class="abs f-head" style="left:434px;top:2308px">NAVIGATION</div>
<ul class="abs f-list" style="left:434px;top:2354px">
  <li><span class="chev">»</span>Home</li><li><span class="chev">»</span>About Us</li><li><span class="chev">»</span>Properties</li><li><span class="chev">»</span>Video</li><li><span class="chev">»</span>Gallery</li><li><span class="chev">»</span>Blog</li><li><span class="chev">»</span>Contact Us</li>
</ul>

<div class="abs f-head" style="left:666px;top:2308px">GET SOCIAL</div>
<ul class="abs f-list f-social" style="left:664px;top:2357px">
  <li><span class="f-circle"></span>Fanpage</li><li><span class="f-circle"></span>Chirper</li><li><span class="f-circle"></span>Circles+</li><li><span class="f-circle"></span>Linkwork</li><li><span class="f-circle"></span>ViewTube</li>
</ul>

<div class="abs f-head" style="left:880px;top:2308px">CONTACT US</div>
<div class="abs contact-row" style="left:880px;top:2360px">
  <span class="contact-icon"><svg width="16" height="20" viewBox="0 0 16 20"><path d="M8 1a6 6 0 0 1 6 6c0 5-6 12-6 12S2 12 2 7a6 6 0 0 1 6-6z" fill="none" stroke="#333" stroke-width="1.8"/><circle cx="8" cy="7" r="2" fill="#333"/></svg></span>
  <div><b>Address:</b><span>Larkfield, North Harbour Row,<br>LKD, 4172</span></div>
</div>
<div class="abs contact-row" style="left:880px;top:2438px">
  <span class="contact-icon"><svg width="12" height="18" viewBox="0 0 12 18"><rect x="1" y="1" width="10" height="16" rx="2" fill="none" stroke="#333" stroke-width="1.8"/></svg></span>
  <div><b>PHONE:</b><span>180 047 9312</span></div>
</div>
<div class="abs contact-row" style="left:880px;top:2498px">
  <span class="contact-icon"><svg width="18" height="14" viewBox="0 0 18 14"><rect x="1" y="1" width="16" height="12" fill="#333"/><path d="M1 1l8 6 8-6" fill="none" stroke="#fff" stroke-width="1.5"/></svg></span>
  <div><b>EMAIL:</b><span>info@hensbyestates.in</span></div>
</div>

<div class="abs footer-bar">© 2016 R &amp; T Hensby Estates. All Rights Reserved.</div>

</body>
</html>
```